We need a postcard design for a new promotion. We are an Australian online store that sells craft mosaic supplies, mainly tiles. View our website to understand more about our product range, www.brightlanecrafts.com.au and what we are about.

This promotion is designed to be used with mosaic studios / classes, as a referral system. They will give these cards to their students who will use them when placing an order. They will enter the studios / classes name during the checkout process. The studio will then receive a credit which will entitle them to receive mosaic supplies.

Target Market(s)

Women aged between 30-65, interest in art & craft

Industry/Entity Type

Store

Requirements
Must have
• Logo
Phone number: 1300 684 157
Website URL: www.brightlanecrafts.com.au

The following wording:

You Can Help Stock Your Studio...
Simply place any order with The Pebblecraft Depot and we will give your studio mosaic supplies, to the value of 10% of your purchase.

Just enter your studios name in the comments box during checkout to ensure your studio receives their supplies.

Studio Name:

```html
<!DOCTYPE html>
<html lang="en">
<head>
<meta charset="utf-8">
<title>The Pebblecraft Depot – Stock Your Studio</title>
<link rel="stylesheet" href="https://fonts.googleapis.com/css2?family=Roboto+Condensed:wght@400;700&display=swap">
<style>
  :root {
    --backdrop: #474747;
    --paper: #ffffff;
    --magenta: #ec3a82;
    --badge-pink: #e5197c;
    --badge-orange: #f6a11a;
    --slate-blue: #5668b3;
    --highlight: #f6ee5a;
    --grey-text: #999a9c;
    --dark-text: #3a3a3a;
    --link-pink: #e0317a;
  }
  * { margin: 0; padding: 0; box-sizing: border-box; }
  html, body {
    width: 962px; height: 1200px; overflow: hidden;
    background: var(--backdrop);
    font-family: "Roboto Condensed", "Arial Narrow", sans-serif;
  }
  .postcard {
    position: absolute; left: 83px; top: 83px;
    width: 797px; height: 1032px;
    background: var(--paper);
    overflow: hidden;
  }
  .hero-photo {
    position: absolute; left: 0; top: 0; width: 797px; height: 457px;
    background:
      radial-gradient(circle at 15% 20%, #e08a2a 0 12%, transparent 28%),
      radial-gradient(circle at 30% 15%, #c7d63c 0 10%, transparent 24%),
      radial-gradient(circle at 65% 20%, #3f9a55 0 8%, transparent 22%),
      radial-gradient(circle at 58% 60%, #cc2a2a 0 10%, transparent 24%),
      radial-gradient(circle at 45% 80%, #4aa8dc 0 8%, transparent 22%),
      radial-gradient(circle at 90% 15%, #b06a32 0 10%, transparent 22%),
      linear-gradient(135deg, #eae7e2, #dedbd6);
  }
  .sale-badge {
    position: absolute; left: 52px; top: 226px;
    width: 210px; height: 210px; border-radius: 50%;
    border: 6px solid var(--paper);
    background: linear-gradient(to bottom, var(--badge-pink) 0 74%, var(--badge-orange) 74% 100%);
    color: var(--paper); font-weight: 700; overflow: hidden;
  }
  .sale-badge .save { position: absolute; left: 34px; top: 20px; font-size: 44px; line-height: 1; }
  .sale-badge .up-to { position: absolute; left: 36px; top: 68px; font-size: 16px; line-height: 1; }
  .sale-badge .amount { position: absolute; left: 33px; top: 84px; font-size: 58px; line-height: 1; letter-spacing: -1px; }
  .sale-badge .amount small { font-size: 26px; letter-spacing: 0; }
  .sale-badge .items { position: absolute; left: 0; right: 0; top: 158px; text-align: center; font-size: 20px; }
  .offer-band {
    position: absolute; left: 0; top: 457px; width: 797px; height: 302px;
    background: var(--magenta); color: var(--paper);
    text-align: center; font-weight: 700; text-transform: uppercase;
    box-shadow: 0 -4px 8px rgba(0,0,0,.35);
  }
  .offer-band h1 { margin-top: 30px; font-size: 66px; line-height: 62px; letter-spacing: 0.5px; }
  .offer-band p { margin-top: 20px; font-size: 22px; line-height: 31px; letter-spacing: 0.3px; }
  .offer-band .accent { color: var(--highlight); }
  .checkout-band {
    position: absolute; left: 0; top: 759px; width: 797px; height: 98px;
    background: var(--slate-blue); color: var(--paper);
    text-align: center; font-weight: 700; text-transform: uppercase;
    font-size: 20px; line-height: 28px; padding-top: 22px;
    box-shadow: 0 -4px 8px rgba(0,0,0,.35);
  }
  .contact {
    position: absolute; left: 54px; top: 888px; text-transform: uppercase;
  }
  .contact .prompt { font-size: 20px; color: var(--dark-text); }
  .contact .phone { font-size: 55px; font-weight: 700; color: var(--grey-text); line-height: 60px; }
  .contact .web { font-size: 21px; color: var(--link-pink); text-transform: none; letter-spacing: 0.5px; }
  .brand {
    position: absolute; left: 476px; top: 930px;
    display: flex; align-items: center; gap: 14px;
  }
  .brand .mark { width: 40px; height: 40px; background: var(--magenta); }
  .brand .name { font-size: 30px; font-weight: 400; color: var(--grey-text); text-transform: uppercase; line-height: 1; }
</style>
</head>
<body>
  <main class="postcard">
    <div class="hero-photo" role="img" aria-label="Photo of colourful glass mosaic tiles, glass pebbles and tile nippers on a white work table"></div>
    <div class="sale-badge">
      <span class="save">SAVE</span>
      <span class="up-to">UP TO</span>
      <span class="amount">50%<small>ON</small></span>
      <span class="items">SALES ITEMS</span>
    </div>
    <section class="offer-band">
      <h1>You can help<br>stock your studio...</h1>
      <p>Simply place any order with <span class="accent">The Pebblecraft Depot</span><br>and we will give your studio mosaic supplies, to the<br>value of <span class="accent">10%</span> of your purchase.</p>
    </section>
    <section class="checkout-band">
      Just enter your studios name in the comments box during<br>checkout to ensure your studio receives their supplies.
    </section>
    <section class="contact">
      <div class="prompt">Visit now to place your order</div>
      <div class="phone">1300 684 157</div>
      <div class="web">www.brightlanecrafts.com.au</div>
    </section>
    <div class="brand">
      <span class="mark"></span>
      <span class="name">The Pebblecraft<br>Depot</span>
    </div>
  </main>
</body>
</html>
```